Manifesto

I want a manifesto with the following five manifestos for our Not for Profit

- We are a For-purpose organisation
- Every service we offer is free
- Every product we sell funds our services
- Every financial transaction is transparent
- Our service is for the greater good
- Our purpose is always to serve the people
- We are a for purpose organisation

Its to go with this website logo/look/feel www.brightlantern.co.nz

Two attachments:

1. I quite like this look/feel of a manifesto (see attached), I want something clean, professional but I also quite like either Retro modern look feel also like a fresh, and uplifting as its for sick people coming to see us and our funds where anyone buys a product are used for helping those who are sick with healing......so needs something conveyed that is fresh, uplifing yet professional.
2. This attachment is how I wrote this down when inspired of how I wanted Bright Lantern to operate. This is our values chart. It has to say

Also check out our website for our logo, look etc.. it doesnt have to be the same but red somewhere would link back to logo. www.brightlantern.co.nz .

```html
<!DOCTYPE html>
<html lang="en">
<head>
<meta charset="utf-8">
<title>Bright Lantern — Manifesto</title>
<link rel="stylesheet" href="https://fonts.googleapis.com/css2?family=Alfa+Slab+One&family=Architects+Daughter&family=Arvo:wght@700&family=Courier+Prime&family=Fredoka:wght@600&family=Questrial&family=Raleway:wght@300&family=Varela+Round&display=swap">
<style>
  :root {
    --paper: #ffffff;
    --panel: #e6e6e6;
    --ink: #111111;
    --caption: #7a7a7a;
    --lime: #8cf21f;
    --red: #f0141e;
    --deep-red: #b0161c;
    --teal: #12aeb0;
    --cyan: #22eef2;
    --sky: #5ff5fa;
    --stone: #8a8a8a;
  }
  html, body {
    margin: 0;
    padding: 0;
    width: 1200px;
    height: 848px;
    overflow: hidden;
    background: var(--paper);
  }
  .manifesto {
    display: block;
    width: 1200px;
    height: 848px;
  }
  .panel { fill: var(--panel); }

  .strapline {
    font-family: "Raleway", sans-serif;
    font-weight: 300;
    font-size: 29px;
    letter-spacing: 3px;
    fill: var(--caption);
  }
  .headline {
    font-family: "Alfa Slab One", serif;
  }
  .headline--every { fill: var(--lime); font-size: 128px; }
  .headline--our { fill: var(--ink); font-size: 118px; }

  .thin {
    font-family: "Questrial", sans-serif;
    fill: var(--ink);
  }
  .script {
    font-family: "Architects Daughter", cursive;
    fill: var(--ink);
  }
  .bold-slab {
    font-family: "Arvo", serif;
    font-weight: 700;
    fill: var(--ink);
  }
  .word-free {
    font-family: "Fredoka", sans-serif;
    font-weight: 600;
    font-size: 118px;
    fill: var(--red);
  }
  .word-funds { fill: var(--teal); font-size: 70px; }
  .word-our-services { fill: var(--cyan); font-size: 40px; }
  .word-transparent {
    font-family: "Alfa Slab One", serif;
    font-size: 84px;
    fill: var(--stone);
  }
  .web-address {
    font-family: "Courier Prime", monospace;
    font-size: 21px;
    fill: var(--ink);
  }
  .round {
    font-family: "Varela Round", sans-serif;
  }
  .word-the-cyan { fill: var(--sky); font-size: 46px; }
  .word-greater { fill: var(--cyan); font-size: 100px; }
  .word-good { fill: var(--teal); font-size: 132px; }
  .word-the-red {
    font-family: "Alfa Slab One", serif;
    font-size: 50px;
    fill: var(--red);
  }
  .word-people {
    font-family: "Alfa Slab One", serif;
    font-size: 104px;
    fill: var(--deep-red);
  }
</style>
</head>
<body>
<svg class="manifesto" viewBox="0 0 1200 848" xmlns="http://www.w3.org/2000/svg" role="img" aria-label="Bright Lantern manifesto">
  <rect class="panel" x="385" y="94" width="405" height="261"/>
  <rect class="panel" x="556" y="490" width="602" height="262"/>

  <text class="strapline" x="40" y="63" textLength="766" lengthAdjust="spacing">WE ARE A FOR PURPOSE ORGANISATION</text>

  <text class="headline headline--every" x="62" y="191" textLength="1095" lengthAdjust="spacingAndGlyphs">EVERY</text>

  <text class="thin" x="115" y="244" font-size="60" textLength="245" lengthAdjust="spacingAndGlyphs">service</text>
  <text class="script" x="148" y="285" font-size="36" textLength="208" lengthAdjust="spacingAndGlyphs">we offer is</text>
  <text class="word-free" x="60" y="366" textLength="296" lengthAdjust="spacingAndGlyphs">Free</text>

  <text class="bold-slab" x="430" y="238" font-size="44" textLength="192" lengthAdjust="spacingAndGlyphs">product</text>
  <text class="thin" x="628" y="254" font-size="36" textLength="132" lengthAdjust="spacingAndGlyphs">we sell</text>
  <text class="script word-funds" x="434" y="302" textLength="196" lengthAdjust="spacingAndGlyphs">funds</text>
  <text class="script word-our-services" x="483" y="345" textLength="280" lengthAdjust="spacingAndGlyphs">our services</text>

  <text class="thin" x="890" y="248" font-size="58" textLength="270" lengthAdjust="spacingAndGlyphs">financial</text>
  <text class="thin" x="840" y="307" font-size="54" textLength="320" lengthAdjust="spacingAndGlyphs">transaction</text>
  <text class="bold-slab" x="1075" y="368" font-size="56" textLength="60" lengthAdjust="spacingAndGlyphs">is</text>
  <text class="word-transparent" x="598" y="425" textLength="562" lengthAdjust="spacingAndGlyphs">transparent</text>

  <text class="web-address" x="115" y="416" textLength="370" lengthAdjust="spacingAndGlyphs">www.brightlantern.co.nz</text>

  <text class="headline headline--our" x="42" y="526" textLength="538" lengthAdjust="spacingAndGlyphs">OUR</text>

  <text class="script" x="42" y="570" font-size="38" textLength="263" lengthAdjust="spacingAndGlyphs">service is for</text>
  <text class="round word-the-cyan" x="310" y="592" textLength="84" lengthAdjust="spacingAndGlyphs">the</text>
  <text class="round word-greater" x="38" y="662" textLength="348" lengthAdjust="spacingAndGlyphs">greater</text>
  <text class="round word-good" x="204" y="740" textLength="318" lengthAdjust="spacingAndGlyphs">good</text>

  <text class="thin" x="612" y="534" font-size="48" textLength="200" lengthAdjust="spacingAndGlyphs">purpose</text>
  <text class="thin" x="775" y="583" font-size="42" textLength="44" lengthAdjust="spacingAndGlyphs">is</text>
  <text class="bold-slab" x="838" y="583" font-size="66" textLength="302" lengthAdjust="spacingAndGlyphs">always</text>
  <text class="script" x="700" y="634" font-size="40" textLength="200" lengthAdjust="spacingAndGlyphs">to serve</text>
  <text class="word-the-red" x="918" y="637" textLength="106" lengthAdjust="spacingAndGlyphs">the</text>
  <text class="word-people" x="732" y="708" textLength="410" lengthAdjust="spacingAndGlyphs">people</text>

  <text class="strapline" x="392" y="806" textLength="766" lengthAdjust="spacing">WE ARE A FOR PURPOSE ORGANISATION</text>
</svg>
</body>
</html>
```